Web design for business website

I need a web design for a business website for one of our clients who is specialized in alarm management software. I would like you to design 3 web pages, one for each of the 3 pages. You need to process the corporate identity of our client to the web design. This means the colors of the logo (red and black) should definitely show up on all of the 3 pages. Find the logo file for the logo of our customer. To increase readability I suggest you use a white/light background. All suggestions are welcome.

Please kindly download atttached Webdesign.zip and read the project brief first. The project brief refers to all other files of the zip file. Your design must have exactly the same structure as the wireframes.
Updates

Target Market(s)

B2B, Alarm management

Industry/Entity Type

Business

Number of Pages Required

3 page

Requirements
Must have
• The web design must have exactly the same structure as the wireframes and needs to contain the colors of the company logo.

```html
<!DOCTYPE html>
<html lang="en">
<head>
<meta charset="utf-8">
<title>Vantrex – Real-time reasoning solutions</title>
<link href="https://fonts.googleapis.com/css2?family=Open+Sans:wght@400;600;700&family=Raleway:wght@300;400;600;700;800&display=swap" rel="stylesheet">
<style>
:root{
  --accent:#e8410f;
  --ink:#1f1f1f;
  --topbar:#161616;
  --nav:#1c1b2d;
  --header-bg:#efefef;
  --footer:#1e1e1e;
  --footer-base:#191919;
  --muted:#6b6b6b;
  --footer-text:#5a5a5a;
  --hero-top:#9a9488;
  --hero-bottom:#7d7a68;
  --white:#fff;
}
*{margin:0;padding:0;box-sizing:border-box}
html,body{width:689px;height:1200px;overflow:hidden;background:#fff}
body{font-family:"Open Sans",sans-serif;color:var(--ink);position:relative}
.abs{position:absolute}
.topbar{left:0;top:0;width:689px;height:24px;background:var(--topbar);color:#cfcfcf;font-size:7px}
.topbar .phone{left:56px;top:7px;display:flex;align-items:center;gap:5px}
.topbar .lang{left:439px;top:8px;font-size:5.5px;white-space:nowrap}
.lang-drop{left:495px;top:4px;width:14px;height:14px;background:var(--accent)}
.lang-val{left:512px;top:4px;width:32px;height:14px;background:#222;color:#999;text-align:center;line-height:14px;font-size:7px}
.search{left:549px;top:4px;width:67px;height:14px;background:#2a2a2a;color:#888;font-size:5px;line-height:14px;padding-left:8px}
.search-btn{left:616px;top:4px;width:17px;height:14px;background:var(--accent)}
.header{left:0;top:24px;width:689px;height:45px;background:var(--header-bg)}
.brand{left:56px;top:31px;display:flex;align-items:center;gap:7px}
.brand-dot{width:26px;height:26px;border-radius:50%;background:var(--accent)}
.brand-name{font-family:Raleway,sans-serif;font-weight:800;font-size:19px;letter-spacing:1px;line-height:1}
.brand-tag{font-size:5.5px;color:#444}
.hbtn{top:32px;height:25px;background:var(--accent);color:#fff;font-size:6.5px;display:flex;align-items:center;justify-content:center;gap:12px;text-transform:uppercase;box-shadow:0 0 0 1px #c9360b}
.nav{left:0;top:69px;width:689px;height:24px;background:var(--nav)}
.nav a{position:absolute;top:0;height:24px;line-height:24px;color:#fff;font-size:6.5px;font-weight:600;text-decoration:none}
.nav a.active{background:var(--accent);top:2px;height:20px;line-height:20px;padding:0 14px;font-weight:700}
.hero{left:0;top:93px;width:689px;height:246px;background:linear-gradient(180deg,var(--hero-top),var(--hero-bottom))}
.hero-box{left:190px;top:146px;width:309px;height:141px;background:rgba(255,255,255,.82);text-align:center}
.kicker{font-family:Raleway,sans-serif;font-weight:700;font-size:10px}
.title{font-family:Raleway,sans-serif;font-weight:400;font-size:15px;color:#222}
.title span{color:var(--accent)}
.hero-box .kicker{margin-top:25px}
.hero-box .title{margin-top:5px}
.hero-box p{font-size:5.3px;color:#444;line-height:1.6;margin:7px 12px 0}
.btn{display:inline-block;background:var(--accent);color:#fff;font-size:6.5px;text-transform:uppercase;height:25px;line-height:25px;width:79px;text-align:center}
.hero-box .btn{margin-top:9px}
.arrow{top:201px;width:29px;height:30px;display:flex;align-items:center;justify-content:center}
.welcome{left:0;top:339px;width:689px;height:349px;background:linear-gradient(180deg,#e6e7ea,#d9dbe0 60%,#cfd1d8);text-align:center}
.welcome .kicker{margin-top:76px}
.welcome .title{font-size:19px;font-weight:300;margin-top:5px}
.rule{width:50px;height:1px;background:var(--accent);margin:12px auto 0}
.welcome p{font-size:6.3px;color:#555;line-height:1.55;width:438px;margin:26px auto 0}
.welcome p+p{margin-top:9px}
.welcome .btn{margin-top:25px}
.clients{left:0;top:688px;width:689px;height:193px;text-align:center}
.clients .kicker{margin-top:47px}
.clients .title{font-size:19px;font-weight:400;margin-top:2px}
.client-row{position:absolute;left:70px;top:130px;width:558px;display:flex;justify-content:space-between;align-items:center}
.client{font-family:Raleway,sans-serif;font-weight:700;font-size:10px;color:#4a4a4a;display:flex;align-items:center;gap:4px}
.client i{width:8px;height:8px;background:var(--accent);border-radius:50%;display:block}
.follow{left:0;top:881px;width:689px;height:122px;background:linear-gradient(180deg,#eef0f4,#e3e6ec)}
.sec-title{font-family:Raleway,sans-serif;font-size:17px;font-weight:400;color:#222}
.sec-title span{color:var(--accent)}
.social{top:64px;width:25px;height:25px;background:#9a9a9a}
.email{left:253px;top:64px;width:310px;height:25px;border:1px solid #1f1f2f;background:rgba(255,255,255,.6);font-size:6.5px;color:#888;line-height:23px;padding-left:14px}
.sub-btn{left:563px;top:64px;width:69px;height:25px;background:var(--nav);color:#fff;font-size:6.5px;font-weight:700;text-align:center;line-height:25px}
.footer{left:0;top:1003px;width:689px;height:167px;background:var(--footer)}
.fcol{top:43px;font-size:6.5px;color:var(--footer-text)}
.fcol h4{font-family:Raleway,sans-serif;font-weight:400;font-size:8.5px;color:#3e3e3e;margin-bottom:10px;text-transform:uppercase}
.fcol li{list-style:none;line-height:11px}
.fcol li.hot{color:var(--accent)}
.fcol .ci{display:flex;align-items:center;gap:8px;line-height:16px}
.base{left:0;top:1170px;width:689px;height:30px;background:var(--footer-base);border-top:1px solid #2a2a2a;text-align:center;font-size:5.5px;color:#444;line-height:30px}
.base span{color:var(--accent)}
</style>
</head>
<body>

<div class="abs topbar">
  <div class="abs phone"><svg width="7" height="7" viewBox="0 0 10 10"><path d="M2 0l2 2.5-1.2 1.2a6 6 0 0 0 3.5 3.5L7.5 6 10 8 8.5 10C4 9.5.5 6 0 1.5z" fill="#cfcfcf"/></svg>+31 (0)20 555 0148</div>
  <div class="abs lang">Selecte Language :</div>
  <div class="abs lang-drop"><svg width="14" height="14"><path d="M5 6h4l-2 2.5z" fill="#fff"/></svg></div>
  <div class="abs lang-val">ENG</div>
  <div class="abs search">Search here...</div>
  <div class="abs search-btn"><svg width="17" height="14"><circle cx="8" cy="6.5" r="2.3" stroke="#fff" stroke-width="1.2" fill="none"/><path d="M9.7 8.2l2 2" stroke="#fff" stroke-width="1.3"/></svg></div>
</div>

<div class="abs header"></div>
<div class="abs brand">
  <div class="brand-dot"></div>
  <div><div class="brand-name">VANTREX</div><div class="brand-tag">Real-time reasoning solutions</div></div>
</div>
<div class="abs hbtn" style="left:415px;width:68px">
  <svg width="7" height="7" viewBox="0 0 10 10"><circle cx="5" cy="3" r="2.5" fill="#fff"/><path d="M0 10a5 4 0 0 1 10 0z" fill="#fff"/></svg>Account</div>
<div class="abs hbtn" style="left:489px;width:69px">
  <svg width="7" height="7" viewBox="0 0 10 10"><rect x="1" y="4.5" width="6" height="5" fill="#fff"/><path d="M3 4.5V2.5a2.5 2.5 0 0 1 5 0" stroke="#fff" stroke-width="1.3" fill="none"/></svg>Log in</div>
<div class="abs hbtn" style="left:564px;width:68px">
  <svg width="7" height="7" viewBox="0 0 10 10"><path d="M0 4h5V2l3 3-3 3V6H0z" fill="#fff"/><path d="M7 1h2v8H7" stroke="#fff" fill="none"/></svg>Sign up</div>

<nav class="abs nav">
  <a class="active" href="#" style="left:56px">HOME</a>
  <a href="#" style="left:128px">INDUSTRY</a>
  <a href="#" style="left:196px">TELECOM</a>
  <a href="#" style="left:263px">POWER</a>
  <a href="#" style="left:323px">UTILITIES</a>
  <a href="#" style="left:388px">INFRA</a>
  <a href="#" style="left:443px">STORE</a>
</nav>

<div class="abs hero" role="img" aria-label="Photograph of an industrial refinery at sunset beside a marsh"></div>
<div class="abs arrow" style="left:27px;background:#ececec"><svg width="8" height="8"><path d="M5 1.5L2.5 4 5 6.5" stroke="var(--accent)" stroke-width="1.5" fill="none"/></svg></div>
<div class="abs arrow" style="left:632px;background:var(--accent)"><svg width="8" height="8"><path d="M3 1.5L5.5 4 3 6.5" stroke="#fff" stroke-width="1.5" fill="none"/></svg></div>
<div class="abs hero-box">
  <div class="kicker">HELLO WE ARE</div>
  <div class="title"><span>VANTREX</span> Real-time reasoning solutions</div>
  <p>Companies have invested to get data out of processes. New technologies have been developed to get real-time data out of the harshest places, like oil-well drill heads or the Great Barrier Riff.</p>
  <a class="btn">Read more</a>
</div>

<section class="abs welcome" role="img" aria-label="Faded photograph of engineers working among industrial pipework">
  <div class="kicker">WELCOME TO</div>
  <div class="title"><span>VANTREX</span> Real-time reasoning solutions</div>
  <div class="rule"></div>
  <p>Companies have invested to get data out of processes. New technologies have been developed to get real-time data out of the harshest places, like oil-well drill heads or the Great Barrier Riff. Data in itself means nothing without the context the data is collected in. Example: data from equipment under maintenance does not provide information to operations. Information - data which is valid and meaningful can overwhelm any user without the proper knowledge to interpret this information.</p>
  <p>Vantrex technology enables easy application of such knowledge in a comprehensible – visual – representation and makes hypothetical reasoning with information possible providing meaningful advisories to subscribers when they need it or when it is required that they are made aware of a situation which requires their attention.</p>
  <a class="btn">Learn more</a>
</section>

<section class="abs clients">
  <div class="kicker">OUR CLIENTS</div>
  <div class="title">THAT <span style="color:var(--accent)">TRUST US</span></div>
  <div class="rule"></div>
  <div class="client-row">
    <div class="client">Norvale</div>
    <div class="client">Pellacorp</div>
    <div class="client"><i></i>Stirmont</div>
    <div class="client"><i></i>Kyrona</div>
    <div class="client">Brewfield</div>
    <div class="client">Ostrava Fuels</div>
    <div class="client"><i></i>Tidewell Oil</div>
  </div>
</section>

<section class="abs follow" role="img" aria-label="Faint photograph of an industrial plant lit at night">
  <div class="abs sec-title" style="left:56px;top:30px">FOLLOW <span>US ON :</span></div>
  <div class="abs social" style="left:56px;background:#3b5998" aria-label="Social profile"></div>
  <div class="abs social" style="left:86px" aria-label="Social profile"></div>
  <div class="abs social" style="left:116px" aria-label="Social profile"></div>
  <div class="abs social" style="left:146px" aria-label="Social profile"></div>
  <div class="abs social" style="left:176px" aria-label="Social profile"></div>
  <div class="abs sec-title" style="left:253px;top:30px">SUBSCRIBE <span>NOW :</span></div>
  <div class="abs email">Enter Your Email Adress</div>
  <div class="abs sub-btn">SUBSCRIBE</div>
</section>

<footer class="abs footer">
  <div class="abs fcol" style="left:56px"><h4>Solutions</h4><ul><li class="hot">VAX Alarm Reporting</li><li>VAX Alarm Analysis</li><li>VAX Alarm Expert</li><li>USE</li></ul></div>
  <div class="abs fcol" style="left:155px"><h4>Industries</h4><ul><li>Industry</li><li>Telecom</li><li>Power</li><li>Utilites</li><li>Infra</li></ul></div>
  <div class="abs fcol" style="left:254px"><h4>About us</h4><ul><li>Company</li><li>Overview</li><li>Leadership</li><li>Partners</li><li>Locations</li></ul></div>
  <div class="abs fcol" style="left:352px"><h4>News</h4><ul><li>Product News</li><li>Partner News</li><li>Events</li><li>Press Releases</li><li>Vacancies</li></ul></div>
  <div class="abs fcol" style="left:500px"><h4>Contact us</h4>
    <div class="ci"><svg width="6" height="6" viewBox="0 0 10 10"><path d="M2 0l2 2.5-1.2 1.2a6 6 0 0 0 3.5 3.5L7.5 6 10 8 8.5 10C4 9.5.5 6 0 1.5z" fill="#5a5a5a"/></svg>+31 (0)20 555 0148</div>
    <div class="ci"><svg width="6" height="6" viewBox="0 0 10 8"><rect width="10" height="8" fill="#5a5a5a"/><path d="M0 0l5 4 5-4" stroke="#1e1e1e" fill="none"/></svg>info@vantrex.example</div>
    <div class="ci"><svg width="6" height="6" viewBox="0 0 8 10"><path d="M4 10L1 5a3.3 3.3 0 1 1 6 0z" fill="#5a5a5a"/></svg>address Vantrex Delft</div>
  </div>
</footer>
<div class="abs base">Copyright © 2105 <span>VANTREX.</span> All Rights Reserved.</div>

</body>
</html>
```